Bright and beautiful business card for a coach

I'm a personal and business coach based in Perth, Australia. I need a business card that whilst subtle and elegant, will stand out and appeal on a table full of cards.

My business name is Fern Coaching and the business card must represent the warmth and brightness implied in the name, without being gimmicky. It must have a warmth and appeal and be easy to read.

I prefer clean, minimalist designs.

It must align with the feel of my website and socials: https://www.ferncoachingplex.com.au/
https://www.instagram.com/ferncoachingplexau/
https://www.facebook.com/ferncoachingplexau
Updates

Deadline appearing 2 days away and still haven't completed brief - seems mighty short

Hi Designers Thank you so much for taking the time to submit designs. I wonder if I could have explained myself a little better. Most of the designs that have been submitted look rather formal and many have quite corporate looking embellishments on them (to my eye). I would like softer, warmer, more organic. I’m open to people playing about and being more abstract, using softer embellishments (e.g the line drawing flowers and grasses I’ve used in my socials) incorporating other colours from my palette or like the social icons in my email signature (in PDF), perhaps playing with size/oversize, playing with the bleed. Please don’t be constrained by what I’ve already done, it merely needs to compliment. I’m sorry if I’m not using the right words or have led you astray. I’m no designer, but I’ve done my website, socials, email signature etc all myself (my logo was a design contest) and I was really hoping for my business card to be something more creative than I could have made with a template. Reminder: No black cards/sides please. Thank you 😊

Target Market(s)

Individuals, most likely but not all female. Creative thinkers. Likely professionals.

Industry/Entity Type

Business & Personal Coach

Contact Information for Business Card

(Fern Coaching Logo) Name: Marla Pendry; Title: Business & Personal Coach; Phone number: +61 (0)498 315807; Email: marla@ferncoachingplex.com.au; Website: https://ferncoachingplex.com.au; Social icons for Facebook, Instagram & LinkedIn: @ferncoachingplexAU. Optional strapline: "A thinking partner to help you cut through the noise"

Font styles to use
Sans Serif

Colors
00AB8E
00BBA5
67D7C9
C6EFE9
E9F9F6
59FF00
82FF00
B8FF75
E3FFCB
F4FFEA
FFC000
F8CF3A
FAE287
FDF2CF
FEFAEE

Requirements
Must have
• Must align with feel of my website and socials. Must have a pop of #FFC000 (possibly whole of one side, or at least a block). Bright or white background. Easy to read.
Nice to have
• Possibly incorporate the sunshine/grass picture I have used in website and socials - will upload.
Should not have
• Must not be black or dark. Not impersonal or corporate looking.

```html
<!DOCTYPE html>
<html lang="en">
<head>
<meta charset="utf-8">
<title>Fern Coaching – Business Card</title>
<link rel="stylesheet" href="https://fonts.googleapis.com/css2?family=Arimo:wght@400;700&display=swap">
<style>
  :root {
    --bg: #ecebe8;
    --white: #ffffff;
    --amber-deep: #d98a1a;
    --amber: #e9a520;
    --amber-bright: #f4c12c;
    --green-deep: #4f7d2a;
    --green-soft: #7fae45;
    --photo-warm: #b89a88;
    --photo-cool: #8f9294;
  }
  * { box-sizing: border-box; margin: 0; padding: 0; }
  html, body {
    width: 1200px; height: 900px; overflow: hidden;
    background: var(--bg);
    font-family: "Arimo", Arial, sans-serif;
  }
  .canvas { position: relative; width: 1200px; height: 900px; }

  .card {
    position: absolute;
    width: 700px; height: 400px;
    border-radius: 22px;
    overflow: hidden;
    box-shadow: 0 10px 28px rgba(0,0,0,0.18);
  }

  /* Back of card */
  .card--back { left: 330px; top: 40px; }
  .back-photo {
    position: absolute; inset: 0;
    background: linear-gradient(180deg, var(--green-deep) 0%, var(--green-soft) 100%);
  }
  .back-logo {
    position: absolute; left: 40px; top: 40px;
    color: var(--white);
    font-weight: 400; font-size: 34px; letter-spacing: 0.08em;
  }
  .strap-band {
    position: absolute; left: 0; right: 0; top: 300px; height: 56px;
    border-top: 12px solid var(--amber-deep);
    border-bottom: 12px solid var(--amber-bright);
    display: flex; align-items: center; justify-content: center;
  }
  .strapline {
    color: var(--white); font-size: 21px; font-weight: 400;
  }

  /* Front of card */
  .card--front { left: 170px; top: 470px; display: flex; }
  .front-photo {
    width: 265px; height: 100%;
    background: linear-gradient(180deg, var(--photo-cool) 0%, var(--photo-warm) 100%);
  }
  .front-panel {
    flex: 1;
    background: linear-gradient(120deg, var(--amber-deep) 0%, var(--amber) 45%, var(--amber-bright) 100%);
    color: var(--white);
    padding: 48px 40px 0 46px;
  }
  .front-logo {
    text-align: center;
    font-size: 40px; font-weight: 400; letter-spacing: 0.08em;
    margin-bottom: 34px;
  }
  .person-name { font-size: 30px; font-weight: 400; letter-spacing: 0.02em; }
  .person-title { font-size: 21px; margin-top: 2px; margin-bottom: 22px; }
  .contact-list { list-style: none; }
  .contact-item {
    display: flex; align-items: center; gap: 10px;
    font-size: 19px; line-height: 1.55;
  }
  .contact-icon { width: 18px; height: 18px; flex: none; }
  .social-mark {
    width: 16px; height: 16px; background: var(--white); border-radius: 3px; flex: none;
  }
</style>
</head>
<body>
<main class="canvas">

  <section class="card card--back">
    <div class="back-photo" role="img" aria-label="Photo of a sunlit grass meadow"></div>
    <div class="back-logo">Fern Coaching</div>
    <div class="strap-band">
      <p class="strapline">A thinking partner to help you cut through the noise</p>
    </div>
  </section>

  <section class="card card--front">
    <div class="front-photo" role="img" aria-label="Portrait photo of the coach"></div>
    <div class="front-panel">
      <div class="front-logo">Fern Coaching</div>
      <h1 class="person-name">MARLA PENDRY</h1>
      <p class="person-title">Business &amp; Personal Coach</p>
      <ul class="contact-list">
        <li class="contact-item">
          <svg class="contact-icon" viewBox="0 0 24 24" aria-hidden="true"><path fill="#fff" d="M6.6 10.8a15 15 0 0 0 6.6 6.6l2.2-2.2a1 1 0 0 1 1-.25 11.4 11.4 0 0 0 3.6.57 1 1 0 0 1 1 1V20a1 1 0 0 1-1 1A17 17 0 0 1 3 4a1 1 0 0 1 1-1h3.5a1 1 0 0 1 1 1c0 1.25.2 2.45.57 3.57a1 1 0 0 1-.25 1z"/></svg>
          +61 (0)498 315807
        </li>
        <li class="contact-item">
          <svg class="contact-icon" viewBox="0 0 24 24" aria-hidden="true"><rect x="2" y="5" width="20" height="14" rx="1.5" fill="none" stroke="#fff" stroke-width="2"/><path d="M2.5 6 12 13l9.5-7" fill="none" stroke="#fff" stroke-width="2"/></svg>
          marla@ferncoachingplex.com.au
        </li>
        <li class="contact-item">
          <svg class="contact-icon" viewBox="0 0 24 24" aria-hidden="true"><circle cx="12" cy="12" r="9.5" fill="none" stroke="#fff" stroke-width="2"/><path d="M2.5 12h19M12 2.5c3 3 3 16 0 19M12 2.5c-3 3-3 16 0 19" fill="none" stroke="#fff" stroke-width="1.6"/></svg>
          www.ferncoachingplex.com.au
        </li>
        <li class="contact-item">
          <span class="social-mark" aria-hidden="true"></span>
          @ferncoachingplexAU
        </li>
      </ul>
    </div>
  </section>

</main>
</body>
</html>
```